A5 Flyer for Financial Services Business

I am after a re-design of our business flyer to fit in with our new branding style and logo colour scheme. Wanting something with a bit of designer flair that I could not create myself. I have included the flyer which I created which lacks style so dazzle me.

I want to use the same content.

Text for main body of flyer is

Are you a small business owner, tradie or PAVC Service Provider struggling to stay on top of your bookkeeping and compliance obligations? If so we would love to help you get back on track and take control of your business finances so that you can make informed business decisions and focus on what you do best.

We have over 20 years industry experience and, as a small business ourselves, we are able to offer our clients a personal bookkeeping solution tailored to meet the needs of your business.

Accounts Payable | Accounts Receivable
Customer Invoicing
Bank and Credit Card Reconciliations
Payroll | Superannuation | Payroll Tax
Business Activity | Instalment Activity Statements
Regular Financial Reports
Ledgro and Tallybook Set-Up and Training

```html
<!DOCTYPE html>
<html lang="en">
<head>
<meta charset="utf-8">
<title>Even Keel Financial Services – Bookkeeping Flyer</title>
<link rel="stylesheet" href="https://fonts.googleapis.com/css2?family=Open+Sans:wght@300;400;600;700&display=swap">
<style>
  :root{
    --teal:#148f96;
    --teal-dark:#0d7b82;
    --teal-light:#2aa8ae;
    --ink:#2b2b2b;
    --grey:#8c9396;
    --white:#ffffff;
  }
  *{margin:0;padding:0;box-sizing:border-box}
  html,body{width:846px;height:1200px;overflow:hidden;background:var(--white)}
  body{font-family:"Open Sans",Arial,sans-serif;color:var(--ink)}
  .flyer{position:relative;width:846px;height:1200px;overflow:hidden}
  .backdrop{position:absolute;inset:0}
  .brand{position:absolute;left:520px;top:118px;width:316px;text-align:center}
  .brand-mark{display:inline-block;width:44px;height:44px;border-radius:50%;background:var(--teal);margin-bottom:14px}
  .brand-name{font-size:30px;font-weight:400;color:var(--teal);letter-spacing:-0.5px;line-height:1.1}
  .brand-sub{font-size:16px;font-weight:400;color:var(--teal);letter-spacing:5px;line-height:1.3}
  .tagline{position:absolute;left:540px;top:244px;width:250px;text-align:center;font-size:24px;font-weight:300;line-height:34px;color:#3a3a3a}
  .intro{position:absolute;left:57px;top:648px;width:742px;font-size:17px;line-height:24.4px;text-align:justify;color:var(--ink)}
  .intro p+p{margin-top:24px}
  .services{position:absolute;left:44px;top:855px;width:759px;height:276px;background:var(--white);border:3px solid var(--teal);border-radius:24px;text-align:center;padding-top:8px}
  .service-list{list-style:none;color:var(--teal);font-weight:600;font-size:17.5px;line-height:24.4px}
  .credentials{display:flex;justify-content:space-between;padding:10px 58px 0 82px;font-size:17.5px;font-weight:600;color:var(--ink)}
  .credential{display:flex;align-items:center;gap:16px}
  .diamond{width:14px;height:14px;transform:rotate(45deg)}
  .diamond.grey{background:var(--grey)}
  .diamond.teal{background:var(--teal)}
  .phone{display:flex;justify-content:center;align-items:center;gap:18px;margin-top:6px;font-size:40px;font-weight:700;color:var(--ink);letter-spacing:1px}
  .website{position:absolute;left:0;top:1150px;width:846px;height:50px;display:flex;justify-content:center;align-items:center;gap:20px;color:var(--white);font-size:26px;font-weight:600}
</style>
</head>
<body>
<main class="flyer">
  <svg class="backdrop" width="846" height="1200" viewBox="0 0 846 1200" aria-hidden="false">
    <defs>
      <linearGradient id="photoTone" x1="0" y1="0" x2="1" y2="1">
        <stop offset="0" stop-color="#c9d3d8"/>
        <stop offset="0.45" stop-color="#8fa0a8"/>
        <stop offset="1" stop-color="#dfe4e6"/>
      </linearGradient>
      <linearGradient id="insetTone" x1="0" y1="0" x2="1" y2="1">
        <stop offset="0" stop-color="#d8c77a"/>
        <stop offset="0.5" stop-color="#7e8a86"/>
        <stop offset="1" stop-color="#3b4144"/>
      </linearGradient>
    </defs>
    <rect x="0" y="0" width="846" height="600" fill="url(#photoTone)" role="img" aria-label="Photo of hands tapping a touch-screen point-of-sale terminal at a counter"/>
    <path d="M0 420 Q120 560 380 592 Q540 606 640 560 L846 560 L846 700 L0 700 Z" fill="var(--teal)"/>
    <path d="M0 520 Q200 600 420 606 Q560 606 640 590 L846 590 L846 700 L0 700 Z" fill="var(--white)"/>
    <circle cx="768" cy="285" r="298" fill="var(--white)" stroke="var(--teal)" stroke-width="5"/>
    <circle cx="690" cy="474" r="124" fill="var(--white)"/>
    <circle cx="690" cy="474" r="116" fill="url(#insetTone)" stroke="var(--teal)" stroke-width="4" role="img" aria-label="Photo of a hand using a touch-screen till with a card reader"/>
    <path d="M0 1000 Q60 985 120 1010 L120 1200 L0 1200 Z" fill="var(--teal)"/>
    <path d="M846 1000 Q786 985 726 1010 L726 1200 L846 1200 Z" fill="var(--teal)"/>
    <rect x="0" y="1150" width="846" height="50" fill="var(--teal-dark)"/>
  </svg>

  <header class="brand">
    <span class="brand-mark"></span>
    <div class="brand-name">EVEN KEEL</div>
    <div class="brand-sub">Financial Services</div>
  </header>

  <h1 class="tagline" style="font-weight:300">Bookkeping Tailored to Your Business Needs</h1>

  <section class="intro">
    <p>Are you a small business owner, tradie or PAVC Service Provider struggling to stay on top of your bookkeeping and compliance obligations? If so we would love to help you get back on track and take control of your business finances so that you can make informed business decisions and focus on what you do best.</p>
    <p>We have over 20 years industry experience and, as a small business ourselves, we are able to offer our clients a personal bookkeeping solution tailored to meet the needs of your business.</p>
  </section>

  <section class="services">
    <ul class="service-list">
      <li>Accounts Payable | Accounts Receivable</li>
      <li>Customer Invoicing</li>
      <li>Bank and Credit Card Reconciliations</li>
      <li>Payroll | Superannuation | Payroll Tax</li>
      <li>Business Activity | Instalment Activity Statements</li>
      <li>Regular Financial Reports</li>
      <li>Ledgro and Tallybook Set-Up and Training</li>
    </ul>
    <div class="credentials">
      <span class="credential"><span class="diamond grey"></span>Ledgro Certified Advisor</span>
      <span class="credential"><span class="diamond teal"></span>Tallybook Pro Advisor</span>
    </div>
    <div class="phone">
      <svg width="30" height="30" viewBox="0 0 24 24" aria-hidden="true"><path fill="#2b2b2b" d="M6.6 10.8a15.1 15.1 0 0 0 6.6 6.6l2.2-2.2a1 1 0 0 1 1-.25 11.4 11.4 0 0 0 3.6.57 1 1 0 0 1 1 1V20a1 1 0 0 1-1 1A17 17 0 0 1 3 4a1 1 0 0 1 1-1h3.5a1 1 0 0 1 1 1c0 1.25.2 2.45.57 3.57a1 1 0 0 1-.25 1z"/></svg>
      <span>0400 518 273</span>
    </div>
  </section>

  <footer class="website">
    <svg width="20" height="20" viewBox="0 0 24 24" aria-hidden="true"><g fill="none" stroke="#fff" stroke-width="2"><circle cx="12" cy="12" r="10"/><path d="M2 12h20M12 2c3 3 3 17 0 20M12 2c-3 3-3 17 0 20"/></g></svg>
    <span>www.evenkeelfinancialservices.com.au</span>
  </footer>
</main>
</body>
</html>
```